How likely are people to engage in social distancing? We need a good illustration to show the data!

We surveyed U.S. adults March 20th - 24th, 2020 and asked how likely they were to engage in social distancing (and other COVID-19 related health behaviors). What did the survey find? Basically, most people intend to engage in social distancing behaviors (e.g., avoiding large crowds) and other behaviors that reduce the spread of COVID-19 (e.g., washing hands at least 20 seconds). When most people intend to engage in a behavior, then public health professionals try to leverage that to move more people to act.
Now we need innovative and professional images that attempt to communicate one or all of these findings. The specific findings are nicely summarized in the attached document. For example, 82% of participants intend to engage in social distancing.
What sort of visual are we looking for? Our preference is for an original illustration (or set of illustrations). Our preference is for (creative and powerful illustrations, but we are also open to the creative and well-executed infographics.
We need these images fast . We will award monetary prizes to the 3 best designs. If we like more than that, then we might purchase more (e.g., in past contests, we have purchased as many as 30 designs).
What we will need:
(1) The illustrations must be original and we will need the photoshop and/or illustrator files for all artwork.
(2) You can illustrate all of the findings or just one of them. We need creative approaches that do a lucid job of bringing the data to life. Most people intend to engage in these behaviors. How to communicate that? Corvantists and Halmerites do not differ in their intentions; how to communicate that?
(3) The illustration should say, somewhere: "Based on a survey of 400 U.S. adults conducted March 20 - 24th, 2020."

U.S. Adults

• Original illustrations based on the findings of the survey (see attached document).

```html
<!DOCTYPE html>
<html lang="en">
<head>
<meta charset="utf-8">
<title>Social Distancing Intentions Survey</title>
<link rel="stylesheet" href="https://fonts.googleapis.com/css2?family=Montserrat+Alternates:wght@800&family=Montserrat:wght@300;400;700&family=Raleway:wght@400;500&display=swap">
<style>
:root{
  --bg:#f3f4f6;
  --ink:#3a3a3a;
  --blue:#2e7fa8;
  --blue-ribbon:#3b80a7;
  --light-teal:#8fc9cc;
  --red:#e0393e;
  --teal:#27bcb0;
  --purple:#8b80c1;
  --gold:#efb336;
  --dark:#474747;
  --frame:#363636;
}
*{margin:0;padding:0;box-sizing:border-box}
html,body{width:1200px;height:2490px;overflow:hidden;background:var(--bg)}
body{position:relative;font-family:"Raleway",sans-serif;color:var(--ink)}
.abs{position:absolute}
.decor{border-radius:50%;background:radial-gradient(circle,#d9d9d9 0%,#e4e5e7 60%,rgba(230,231,233,0) 72%)}
.title{font-family:"Montserrat Alternates",sans-serif;font-weight:800;font-size:46px;line-height:46px;color:var(--ink);left:44px}
.title .n{font-family:"Montserrat",sans-serif;font-weight:300;color:var(--light-teal)}
.title.blue{color:var(--blue)}
.lead{font-family:"Montserrat Alternates",sans-serif;font-weight:800;font-size:23px;left:45px;top:142px;color:var(--ink)}
.question{font-family:"Montserrat",sans-serif;font-weight:400;font-size:22px;line-height:24px;color:var(--blue);left:45px}
.stat{position:absolute;width:560px}
.stat-label{font-family:"Raleway",sans-serif;font-weight:500;font-size:24px;line-height:30px;letter-spacing:-.3px;text-transform:uppercase;height:60px;display:flex;align-items:flex-end}
.stat-row{display:flex;align-items:center;margin-top:6px}
.battery{position:relative;width:228px;height:62px;border:4px solid var(--frame);border-radius:3px;padding:6px;display:flex;gap:4px;background:#fff}
.battery::after{content:"";position:absolute;right:-13px;top:14px;width:9px;height:26px;background:var(--frame);border-radius:0 2px 2px 0}
.battery span{flex:1;background:var(--c);border-radius:1px}
.battery span.off{background:var(--dark)}
.stat-value{font-family:"Montserrat",sans-serif;font-weight:400;font-size:62px;margin-left:24px;color:var(--c)}
.stat,.stat-label{color:var(--c)}
.ribbon{position:absolute;height:38px;background:var(--blue-ribbon);color:#fff;font-family:"Montserrat Alternates",sans-serif;font-weight:800;font-size:23px;line-height:38px;padding-left:42px;clip-path:polygon(0 0,100% 0,96% 50%,100% 100%,0 100%,4% 50%)}
.answer{position:absolute;font-family:"Raleway",sans-serif;font-weight:500;font-size:23px;text-transform:uppercase;color:var(--ink);border-bottom:2px solid var(--ink);padding:0 6px 4px}
.illustration{left:150px;top:975px;width:900px;height:250px;border-radius:24px;background:linear-gradient(90deg,#d4e4ec 0%,#b8d3e1 45%,#d4e4ec 100%)}
.col-head{position:absolute;top:1484px;font-family:"Montserrat",sans-serif;font-weight:700;font-size:30px;color:var(--ink);letter-spacing:.5px}
.compare{position:absolute;left:0;width:1200px;height:91px}
.compare-label{position:absolute;top:0;width:100%;text-align:center;font-family:"Raleway",sans-serif;font-weight:500;font-size:24px;color:var(--c);text-transform:uppercase;letter-spacing:-.3px}
.track{position:absolute;top:40px;height:34px;width:390px;background:var(--dark);border-radius:3px;overflow:hidden}
.track.left{left:112px}
.track.right{left:671px}
.fill{position:absolute;top:0;height:100%;background:var(--c);width:calc(var(--p)*1% - 6%)}
.track.left .fill{left:0}
.track.right .fill{right:0}
.dot{position:absolute;top:23px;width:68px;height:68px;border-radius:50%;background:var(--c);border:4px solid #3b3b3b;color:#fff;font-family:"Montserrat",sans-serif;font-weight:400;font-size:19px;display:flex;align-items:center;justify-content:center}
.dot.left{left:48px}
.dot.right{left:1056px}
.red{--c:var(--red)}
.teal{--c:var(--teal)}
.purple{--c:var(--purple)}
.gold{--c:var(--gold)}
</style>
</head>
<body>

<div class="abs decor" role="img" aria-label="Faint virus particle decoration" style="left:930px;top:-20px;width:200px;height:200px"></div>
<div class="abs decor" role="img" aria-label="Faint virus particle decoration" style="left:960px;top:870px;width:260px;height:260px"></div>
<div class="abs decor" role="img" aria-label="Faint virus particle decoration" style="left:-40px;top:1030px;width:230px;height:230px"></div>
<div class="abs decor" role="img" aria-label="Faint virus particle decoration" style="left:1010px;top:2340px;width:200px;height:200px"></div>

<h1 class="abs title" style="top:28px">Survey of U.S. Adults <span class="n">(N=400)</span></h1>
<h2 class="abs title blue" style="top:75px">Conducted March 20th - 24th, 2020</h2>
<p class="abs lead">Percent of Americans intending to engage in social distancing</p>
<p class="abs question" style="top:178px">We would like to know how likely it is that you will perform these behaviors<br>to slow the spread of coronavirus?</p>

<section>
  <div class="stat red" style="left:42px;top:256px">
    <div class="stat-label">Engage in social<br>distancing</div>
    <div class="stat-row"><div class="battery"><span></span><span></span><span></span><span></span><span></span><span></span><span></span><span></span><span class="off"></span><span class="off"></span></div><div class="stat-value">82%</div></div>
  </div>
  <div class="stat red" style="left:651px;top:256px">
    <div class="stat-label">Wash hands at<br>least 20 seconds</div>
    <div class="stat-row"><div class="battery"><span></span><span></span><span></span><span></span><span></span><span></span><span></span><span></span><span></span><span class="off"></span></div><div class="stat-value">87%</div></div>
  </div>
  <div class="stat teal" style="left:42px;top:383px">
    <div class="stat-label">Work from home</div>
    <div class="stat-row"><div class="battery"><span></span><span></span><span></span><span></span><span></span><span></span><span class="off"></span><span class="off"></span><span class="off"></span><span class="off"></span></div><div class="stat-value">63%</div></div>
  </div>
  <div class="stat teal" style="left:651px;top:383px">
    <div class="stat-label">Cancel social activities</div>
    <div class="stat-row"><div class="battery"><span></span><span></span><span></span><span></span><span></span><span></span><span></span><span></span><span class="off"></span><span class="off"></span></div><div class="stat-value">81%</div></div>
  </div>
  <div class="stat purple" style="left:42px;top:509px">
    <div class="stat-label">Avoid large gatherings</div>
    <div class="stat-row"><div class="battery"><span></span><span></span><span></span><span></span><span></span><span></span><span></span><span></span><span class="off"></span><span class="off"></span></div><div class="stat-value">85%</div></div>
  </div>
  <div class="stat purple" style="left:651px;top:509px">
    <div class="stat-label">Use hand sanitizer</div>
    <div class="stat-row"><div class="battery"><span></span><span></span><span></span><span></span><span></span><span></span><span></span><span></span><span class="off"></span><span class="off"></span></div><div class="stat-value">85%</div></div>
  </div>
  <div class="stat gold" style="left:42px;top:664px">
    <div class="stat-label">Put distance between<br>yourself and other people</div>
    <div class="stat-row"><div class="battery"><span></span><span></span><span></span><span></span><span></span><span></span><span></span><span></span><span class="off"></span><span class="off"></span></div><div class="stat-value">85%</div></div>
  </div>
  <div class="stat gold" style="left:651px;top:664px">
    <div class="stat-label">Avoid touching your<br>eyes, nose, and mouth</div>
    <div class="stat-row"><div class="battery"><span></span><span></span><span></span><span></span><span></span><span></span><span></span><span></span><span class="off"></span><span class="off"></span></div><div class="stat-value">81%</div></div>
  </div>
</section>

<div class="ribbon" style="left:38px;top:847px;width:428px">What does this data say?</div>
<p class="answer" style="left:38px;top:895px;width:895px">It says that most people intend to engage in these behaviors.</p>

<div class="abs illustration" role="img" aria-label="Illustration: map of the United States with outbreak hotspots, surrounded by icons of a warning sign, hand washing, a home, lungs and a virus"></div>

<h2 class="abs title" style="top:1273px">Comparing Corvantists and Halmerites</h2>
<h2 class="abs title blue" style="top:1320px">March 20th - 24th, 2020 Survey</h2>
<p class="abs question" style="top:1397px">We would like to know how likely it is that you will perform these behaviors<br>to slow the spread of coronavirus?</p>

<div class="col-head" style="left:134px">CORVANTIST</div>
<div class="col-head" style="left:805px">HALMERITE</div>

<section>
  <div class="compare red" style="top:1534px"><div class="compare-label">Engage in social distancing</div>
    <div class="track left" style="--p:82"><div class="fill"></div></div><div class="dot left">82%</div>
    <div class="track right" style="--p:81"><div class="fill"></div></div><div class="dot right">81%</div></div>
  <div class="compare teal" style="top:1625px"><div class="compare-label">Work from home</div>
    <div class="track left" style="--p:60"><div class="fill"></div></div><div class="dot left">60%</div>
    <div class="track right" style="--p:65"><div class="fill"></div></div><div class="dot right">65%</div></div>
  <div class="compare purple" style="top:1716px"><div class="compare-label">Avoid large gatherings</div>
    <div class="track left" style="--p:85"><div class="fill"></div></div><div class="dot left">85%</div>
    <div class="track right" style="--p:84"><div class="fill"></div></div><div class="dot right">84%</div></div>
  <div class="compare gold" style="top:1807px"><div class="compare-label">Put distance between yourself and other people</div>
    <div class="track left" style="--p:84"><div class="fill"></div></div><div class="dot left">84%</div>
    <div class="track right" style="--p:87"><div class="fill"></div></div><div class="dot right">87%</div></div>
  <div class="compare red" style="top:1898px"><div class="compare-label">Wash hands at least 20 seconds</div>
    <div class="track left" style="--p:87"><div class="fill"></div></div><div class="dot left">87%</div>
    <div class="track right" style="--p:88"><div class="fill"></div></div><div class="dot right">88%</div></div>
  <div class="compare teal" style="top:1989px"><div class="compare-label">Cancel social activities</div>
    <div class="track left" style="--p:82"><div class="fill"></div></div><div class="dot left">82%</div>
    <div class="track right" style="--p:80"><div class="fill"></div></div><div class="dot right">80%</div></div>
  <div class="compare purple" style="top:2080px"><div class="compare-label">Use hand sanitizer</div>
    <div class="track left" style="--p:87"><div class="fill"></div></div><div class="dot left">87%</div>
    <div class="track right" style="--p:84"><div class="fill"></div></div><div class="dot right">84%</div></div>
  <div class="compare gold" style="top:2171px"><div class="compare-label">Avoid touching your eyes, nose, and mouth</div>
    <div class="track left" style="--p:80"><div class="fill"></div></div><div class="dot left">80%</div>
    <div class="track right" style="--p:82"><div class="fill"></div></div><div class="dot right">82%</div></div>
</section>

<div class="ribbon" style="left:84px;top:2313px;width:428px">What does this data say?</div>
<p class="answer" style="left:84px;top:2362px;width:692px">No big differences. Basically the same patterns.</p>

</body>
</html>
```